Delivery Company / Logistics Company Flyer

Im looking for something I can mail out to my current and potential customers highlighting our services, history, service locations, and contact information.(see uploaded DOC)
Website: http://www.kalvontransit.com/
About:
• 35 years in the delivery business Kalvon provides a custom logistics solution to each customer’s needs. Led by an experienced leadership group and a very versatile operations team Kalvon Provides the “boutique” solution to their customers’ vs. The cookie cutter service the majority of the industry provides.
Assets:
• We have a tremendous group of drivers operating over 100 assets ranging from Courier Vans to 53ft Tractor trailers.
Markets Serviced:
• Dallas TX
• Kansas City MO
• St. Louis MO
Services:
• White Glove Deliveries
• Home Delivery
• B2B
• B2C
• Airport Transfers
• Cross dock and Warehousing Logistics
• Courier Deliveries
• Pharmaceutical Deliveries
• Dedicated Services
Associations:
• BFX Certified Carrier
• Green Route Haulage Partner
• NMU (national movers union)
Contact information:
Dean Marwick – Sales
Mobile: 940.555.0186
Email: dmarwick@kvtx.example and sales@kvtx.example
Target Market(s)
Shipping companies in Dallas TX, Kansas City MO and St. Louis MO.(see uploaded DOC)
Industry/Entity Type
Trucking Company
Requirements
Must have
- Points on the US map where we service Dallas TX, Kansas City MO and St. Louis MO. Contact info, services we proved, assets, brief history.(see uploaded DOC)
Nice to have
- Associations (see uploaded DOC)

```html
<!DOCTYPE html>
<html lang="en">
<head>
<meta charset="utf-8">
<title>Kalvon Logistics Flyer</title>
<link href="https://fonts.googleapis.com/css2?family=Anton&family=Lato:wght@400;700;900&display=swap" rel="stylesheet">
<style>
:root{
  --red:#e8262a;
  --orange:#f7941d;
  --amber:#fbb03b;
  --yellow:#f5b820;
  --ink:#1e1e1e;
  --dark:#3a3a3a;
  --paper:#ffffff;
  --bg:#dcdad6;
}
*{margin:0;padding:0;box-sizing:border-box}
html,body{width:1200px;height:1200px;overflow:hidden;background:var(--bg)}
body{font-family:'Lato',sans-serif;color:var(--ink)}
.flyer{position:absolute;left:150px;top:18px;width:900px;height:1165px;background:var(--paper);overflow:hidden;box-shadow:0 6px 24px rgba(0,0,0,.25)}
.abs{position:absolute}
.hero-art{position:absolute;left:0;top:0;width:900px;height:620px}
.bottom-band{position:absolute;left:0;top:905px;width:900px;height:260px}
.brand{left:36px;top:88px;display:flex;align-items:center;gap:10px}
.brand-dot{width:22px;height:22px;border-radius:50%;background:var(--yellow)}
.brand-name{font-weight:900;font-size:28px;line-height:1.05;color:var(--ink)}
.headline{left:210px;top:42px;font-family:'Anton',sans-serif;font-weight:400;font-size:34px;letter-spacing:.5px;color:var(--ink);white-space:nowrap}
.headline .accent{color:var(--red)}
.section-title{font-weight:900;font-size:26px;line-height:1.2;color:var(--red);letter-spacing:.5px;margin-bottom:6px;white-space:nowrap}
.body-text{font-size:15px;line-height:1.45;color:var(--ink)}
.about{left:40px;top:598px;width:510px}
.about .body-text{text-align:justify}
.assets{left:40px;top:750px;width:400px}
.markets{left:40px;top:838px}
.tick-list{list-style:none}
.tick-list li{display:flex;align-items:center;gap:12px;font-size:17px;margin-bottom:7px}
.tick{width:18px;height:18px;flex:none}
.services{left:570px;top:468px;width:310px;height:272px;background:var(--red);border-radius:14px;padding:48px 18px 0 26px}
.services-tag{position:absolute;left:-20px;top:12px;background:var(--yellow);color:var(--ink);font-weight:900;font-size:20px;padding:4px 22px 4px 26px}
.services .tick-list li{color:#fff;font-weight:700;font-size:13.5px;margin-bottom:4px;align-items:flex-start;gap:10px}
.services .tick{width:15px;height:15px;margin-top:1px}
.associations{left:470px;top:752px;width:230px}
.badge{width:180px;height:38px;border:1px solid #bbb;border-radius:6px;background:#fff;margin-bottom:8px;display:flex;align-items:center;justify-content:center;box-shadow:0 1px 3px rgba(0,0,0,.15)}
.badge span{display:block;width:110px;height:14px;border-radius:3px}
.badge.one span{background:#2b4aa0}
.badge.two span{background:#c9242b}
.badge.three span{background:#3aa56a}
.map-area{left:715px;top:772px;width:165px;height:118px;border-radius:26px 10px 34px 18px;background:linear-gradient(90deg,#6b6b6b 0 40%,var(--orange) 40% 100%)}
.person{left:40px;top:1078px}
.person-name{font-weight:900;font-size:40px;color:var(--dark);line-height:1;white-space:nowrap}
.person-role{font-weight:700;font-size:20px;color:var(--dark)}
.contact-row{left:310px;top:1018px;width:575px;display:flex;align-items:center;justify-content:space-between}
.contact-item{display:flex;align-items:center;gap:8px;font-weight:700;color:var(--dark);white-space:nowrap}
.contact-item .icon{width:26px;height:26px;flex:none}
.phone{font-size:22px;font-weight:900}
.emails{font-size:13px;line-height:1.3}
.web{font-size:13px}
</style>
</head>
<body>
<main class="flyer">
  <svg class="hero-art" viewBox="0 0 900 620" role="img" aria-label="Photo of a white tractor trailer on a highway at sunset">
    <defs>
      <linearGradient id="swoosh" x1="0" y1="0" x2="1" y2="1">
        <stop offset="0" stop-color="#fbb03b"/>
        <stop offset="0.5" stop-color="#f7941d"/>
        <stop offset="1" stop-color="#e8262a"/>
      </linearGradient>
      <linearGradient id="photo" x1="0" y1="0" x2="0" y2="1">
        <stop offset="0" stop-color="#f3e7cf"/>
        <stop offset="0.45" stop-color="#c9a46a"/>
        <stop offset="0.75" stop-color="#7a6340"/>
        <stop offset="1" stop-color="#3d3226"/>
      </linearGradient>
    </defs>
    <ellipse cx="470" cy="362" rx="478" ry="222" fill="url(#swoosh)"/>
    <ellipse cx="420" cy="358" rx="470" ry="212" fill="url(#photo)"/>
  </svg>

  <div class="abs brand"><span class="brand-dot"></span><span class="brand-name">Kalvon<br>Logistics</span></div>
  <h1 class="abs headline">Driven to Deliver Customer <span class="accent">Satisfaction</span></h1>

  <section class="abs services">
    <div class="services-tag">SERVICES</div>
    <ul class="tick-list">
      <li><svg class="tick" viewBox="0 0 20 20"><circle cx="10" cy="10" r="8.5" fill="none" stroke="#f5b820" stroke-width="2"/><path d="M6 10.5l3 3 5-6" fill="none" stroke="#f5b820" stroke-width="2"/></svg>White Glove Deliveries</li>
      <li><svg class="tick" viewBox="0 0 20 20"><circle cx="10" cy="10" r="8.5" fill="none" stroke="#f5b820" stroke-width="2"/><path d="M6 10.5l3 3 5-6" fill="none" stroke="#f5b820" stroke-width="2"/></svg>Home Delivery</li>
      <li><svg class="tick" viewBox="0 0 20 20"><circle cx="10" cy="10" r="8.5" fill="none" stroke="#f5b820" stroke-width="2"/><path d="M6 10.5l3 3 5-6" fill="none" stroke="#f5b820" stroke-width="2"/></svg>B2B</li>
      <li><svg class="tick" viewBox="0 0 20 20"><circle cx="10" cy="10" r="8.5" fill="none" stroke="#f5b820" stroke-width="2"/><path d="M6 10.5l3 3 5-6" fill="none" stroke="#f5b820" stroke-width="2"/></svg>B2C</li>
      <li><svg class="tick" viewBox="0 0 20 20"><circle cx="10" cy="10" r="8.5" fill="none" stroke="#f5b820" stroke-width="2"/><path d="M6 10.5l3 3 5-6" fill="none" stroke="#f5b820" stroke-width="2"/></svg>Airport Transfers</li>
      <li><svg class="tick" viewBox="0 0 20 20"><circle cx="10" cy="10" r="8.5" fill="none" stroke="#f5b820" stroke-width="2"/><path d="M6 10.5l3 3 5-6" fill="none" stroke="#f5b820" stroke-width="2"/></svg>Cross dock and Warehousing Logistics</li>
      <li><svg class="tick" viewBox="0 0 20 20"><circle cx="10" cy="10" r="8.5" fill="none" stroke="#f5b820" stroke-width="2"/><path d="M6 10.5l3 3 5-6" fill="none" stroke="#f5b820" stroke-width="2"/></svg>Courier Deliveries</li>
      <li><svg class="tick" viewBox="0 0 20 20"><circle cx="10" cy="10" r="8.5" fill="none" stroke="#f5b820" stroke-width="2"/><path d="M6 10.5l3 3 5-6" fill="none" stroke="#f5b820" stroke-width="2"/></svg>Pharmaceutical Deliveries</li>
      <li><svg class="tick" viewBox="0 0 20 20"><circle cx="10" cy="10" r="8.5" fill="none" stroke="#f5b820" stroke-width="2"/><path d="M6 10.5l3 3 5-6" fill="none" stroke="#f5b820" stroke-width="2"/></svg>Dedicated Services</li>
    </ul>
  </section>

  <section class="abs about">
    <h2 class="section-title">ABOUT</h2>
    <p class="body-text">35 years in the delivery business Kalvon provides a custom logistics solution to each customer’s needs. Led by an experienced leadership group and a very versatile operations team Kalvon Provides the “boutique” solution to their customers’ vs. The cookie cutter service the majority of the industry provides.</p>
  </section>

  <section class="abs assets">
    <h2 class="section-title">ASSETS</h2>
    <p class="body-text">We have a tremendous group of drivers operating over 100 assets ranging from Courier Vans to 53ft Tractor trailers.</p>
  </section>

  <section class="abs markets">
    <h2 class="section-title">MARKETS SERVICED</h2>
    <ul class="tick-list">
      <li><svg class="tick" viewBox="0 0 20 20"><circle cx="10" cy="10" r="8.5" fill="none" stroke="#f5b820" stroke-width="2"/><path d="M6 10.5l3 3 5-6" fill="none" stroke="#f5b820" stroke-width="2"/></svg>Dallas TX</li>
      <li><svg class="tick" viewBox="0 0 20 20"><circle cx="10" cy="10" r="8.5" fill="none" stroke="#f5b820" stroke-width="2"/><path d="M6 10.5l3 3 5-6" fill="none" stroke="#f5b820" stroke-width="2"/></svg>Kansas City MO</li>
      <li><svg class="tick" viewBox="0 0 20 20"><circle cx="10" cy="10" r="8.5" fill="none" stroke="#f5b820" stroke-width="2"/><path d="M6 10.5l3 3 5-6" fill="none" stroke="#f5b820" stroke-width="2"/></svg>St. Louis MO</li>
    </ul>
  </section>

  <section class="abs associations">
    <h2 class="section-title">ASSOCIATIONS</h2>
    <div class="badge one"><span></span></div>
    <div class="badge two"><span></span></div>
    <div class="badge three"><span></span></div>
  </section>

  <div class="abs map-area" role="img" aria-label="Map of the United States with the service region around Dallas, Kansas City and St. Louis highlighted in orange"></div>

  <svg class="bottom-band" viewBox="0 0 900 260" aria-hidden="true">
    <defs>
      <linearGradient id="band" x1="0" y1="1" x2="1" y2="0">
        <stop offset="0" stop-color="#f7941d"/>
        <stop offset="1" stop-color="#fbb03b"/>
      </linearGradient>
    </defs>
    <path d="M0 150 Q450 60 900 20 L900 260 L0 260 Z" fill="url(#band)"/>
  </svg>

  <div class="abs person">
    <div class="person-name">DEAN MARWICK</div>
    <div class="person-role">Sales</div>
  </div>

  <footer class="abs contact-row">
    <div class="contact-item">
      <svg class="icon" viewBox="0 0 30 30"><circle cx="15" cy="15" r="13" fill="none" stroke="#3a3a3a" stroke-width="2"/><path d="M10 9c0 7 4 11 11 11l1-3-3-1.5-1.5 1.5c-2-1-3.5-2.5-4.5-4.5L14.5 11 13 8z" fill="#3a3a3a"/></svg>
      <span class="phone">940.555.0186</span>
    </div>
    <div class="contact-item">
      <svg class="icon" viewBox="0 0 30 30"><circle cx="15" cy="15" r="13" fill="none" stroke="#3a3a3a" stroke-width="2"/><rect x="8" y="10" width="14" height="10" fill="#3a3a3a"/><path d="M8 10l7 6 7-6" fill="none" stroke="#f7941d" stroke-width="1.5"/></svg>
      <span class="emails">dmarwick@kvtx.example<br>sales@kvtx.example</span>
    </div>
    <div class="contact-item">
      <svg class="icon" viewBox="0 0 30 30"><circle cx="15" cy="15" r="13" fill="none" stroke="#3a3a3a" stroke-width="2"/><circle cx="15" cy="15" r="7" fill="none" stroke="#3a3a3a" stroke-width="1.5"/><path d="M8 15h14M15 8c-3 4-3 10 0 14M15 8c3 4 3 10 0 14" fill="none" stroke="#3a3a3a" stroke-width="1.2"/></svg>
      <span class="web">www.kalvontransit.com</span>
    </div>
  </footer>
</main>
</body>
</html>
```